KAVELUXE Consultancy Business Card

We need a business card design for a new Image & Etiquette Consultancy Company.

The design should reflect the corporate colour found in the logo attached.

Info to include:

Name: Marelda Quon
Title: Image Consultant
Company: KA VELUXE CONSULTANCY
Address: 27 Pelham Street, #14-08 Harbourview Tower, Singapore 048215
Contact: 9317 6408
Email: marelda@kaveluxe.com.sg
Website: www.kaveluxe.com.sg

Industry/Entity Type

Business

```html
<!DOCTYPE html>
<html lang="en">
<head>
<meta charset="utf-8">
<title>KA VELUXE Consultancy – Business Card</title>
<link rel="stylesheet" href="https://fonts.googleapis.com/css2?family=Carlito:wght@400;700&display=swap">
<style>
  :root {
    --backdrop: #e9e6ee;
    --card-white: #ffffff;
    --plum: #2b1547;
    --gold: #c9a23a;
    --ink: #1e1e1e;
    --on-plum: #ffffff;
  }
  * { margin: 0; padding: 0; box-sizing: border-box; }
  html, body { width: 1200px; height: 900px; overflow: hidden; }
  body {
    background: var(--backdrop);
    font-family: "Carlito", "Calibri", sans-serif;
    position: relative;
  }
  .card {
    position: absolute;
    width: 700px;
    height: 401px;
    border-radius: 24px;
    overflow: hidden;
  }
  .card-front { left: 52px; top: 26px; background: var(--card-white); color: var(--ink); }
  .card-back  { left: 460px; top: 467px; background: var(--plum); }

  .brand-name {
    font-family: "Carlito", "Calibri", sans-serif;
    font-weight: 400;
    letter-spacing: 2px;
    white-space: nowrap;
  }
  .card-front .brand-name {
    position: absolute; left: 50px; top: 62px;
    font-size: 46px; color: var(--plum);
  }
  .contact-list { position: absolute; left: 41px; top: 155px; list-style: none; }
  .contact-list li {
    display: flex; align-items: center; gap: 9px;
    font-size: 17px; height: 23.5px;
  }
  .contact-list svg { width: 15px; height: 15px; flex: none; }
  .address {
    position: absolute; left: 41px; top: 245px;
    font-size: 17px; line-height: 24px; font-style: normal;
  }
  .wave { position: absolute; left: 0; bottom: 0; width: 700px; height: 401px; }
  .signature {
    position: absolute; right: 87px; bottom: 22px;
    color: var(--on-plum); font-size: 16px; white-space: nowrap;
  }
  .signature strong { font-size: 20px; font-weight: 700; }

  .card-back .brand-name {
    position: absolute; left: 0; right: 0; top: 140px;
    text-align: center; font-size: 52px; color: var(--gold);
  }
  .card-back .website {
    position: absolute; left: 0; right: 0; top: 296px;
    text-align: center; color: var(--on-plum); font-size: 21px;
  }
</style>
</head>
<body>

<section class="card card-front" aria-label="Business card front">
  <div class="brand-name">KA VELUXE</div>

  <ul class="contact-list">
    <li>
      <svg viewBox="0 0 16 16" aria-hidden="true"><circle cx="8" cy="8" r="7" fill="none" stroke="#1e1e1e" stroke-width="1.2"/><path d="M5.5 4.5c-.8.8 0 3.4 1.8 5.2s4.4 2.6 5.2 1.8l-1.6-1.6-1.2.8C8.6 10.2 7 8.6 6.5 7.6l.8-1.2z" fill="#1e1e1e"/></svg>
      9317 6408
    </li>
    <li>
      <svg viewBox="0 0 16 16" aria-hidden="true"><path d="M1.5 6.5 8 2l6.5 4.5V14h-13z" fill="none" stroke="#1e1e1e" stroke-width="1.4"/><path d="M1.5 6.5 8 10.5l6.5-4" fill="none" stroke="#1e1e1e" stroke-width="1.4"/></svg>
      marelda@kaveluxe.com.sg
    </li>
    <li>
      <svg viewBox="0 0 16 16" aria-hidden="true"><g fill="none" stroke="#1e1e1e" stroke-width="1.2"><circle cx="8" cy="8" r="6.5"/><ellipse cx="8" cy="8" rx="3" ry="6.5"/><path d="M1.5 8h13M2.5 4.8h11M2.5 11.2h11"/></g></svg>
      www.kaveluxe.com.sg
    </li>
  </ul>

  <address class="address">
    27 Pelham Street, #14-08<br>
    Harbourview Tower, Singapore<br>
    048215
  </address>

  <svg class="wave" viewBox="0 0 700 401" aria-hidden="true">
    <path d="M0 392 C200 346 430 326 700 340 L700 401 L0 401 Z" fill="var(--plum)"/>
    <path d="M0 380 C200 334 430 314 700 328" fill="none" stroke="var(--gold)" stroke-width="5"/>
  </svg>

  <p class="signature"><strong>Marelda Quon,</strong> Image Consultant</p>
</section>

<section class="card card-back" aria-label="Business card back">
  <div class="brand-name">KA VELUXE</div>
  <p class="website">www.kaveluxe.com.sg</p>
</section>

</body>
</html>
```